Forge Night Club Flyer, need asap for party this weekend

Need a flyer for club night this Saturday. Guaranteed project need quick turnaround. Image attached, and the FORGE logo to be large and detailed like a sign. The dj names PARALLAX, MR. HALVERTON, AND DESMOND K. FARLEY can be large too. It's for house/electronic music in a nice classy venue. High Res image attached.

Target Market(s)

21-40 year old house music lovers, club business

Industry/Entity Type

Night Club

Font styles to use
Sans Serif

Colors
ffffff
cadf82
33a6d7
0356a4
fbee3d

Requirements
Must have
• Either the girl in hard hat or tool belt image, or something similar to stick with the Forge theme. Also the dj names needs to be the same size
Nice to have
• Faded image or some lining around the images so it doesn't look like a plain photo. Black and white is good or faded.
Should not have
• Any cursive or anything not professional looking

```html
<!DOCTYPE html>
<html lang="en">
<head>
<meta charset="utf-8">
<title>Forge – Club Night Flyer</title>
<link rel="stylesheet" href="https://fonts.googleapis.com/css2?family=Arimo:wght@400;700&display=swap">
<style>
  :root {
    --page: #ffffff;
    --white: #ffffff;
    --lime: #c6dc5c;
    --cream: #eef4c6;
    --green: #9ccf4a;
    --aqua: #3cc1b0;
    --cyan: #22c0e0;
    --photo-light: #b4c846;
    --photo-mid: #94b466;
    --photo-shade: #7f9a78;
  }
  html, body {
    margin: 0;
    width: 1200px;
    height: 979px;
    overflow: hidden;
    background: var(--page);
  }
  .flyer {
    position: absolute;
    left: 146px;
    top: 154px;
    width: 904px;
    height: 658px;
    display: block;
    font-family: "Arimo", "Helvetica Neue", Arial, sans-serif;
  }
  .wordmark { font-weight: 700; font-size: 210px; letter-spacing: -8px; fill: var(--white); }
  .date { font-weight: 400; font-size: 35px; letter-spacing: -0.5px; fill: var(--white); }
  .venue { font-weight: 700; font-size: 54px; letter-spacing: -2px; fill: var(--lime); }
  .tagline { font-weight: 400; font-size: 23px; fill: var(--white); }
  .dj { font-weight: 700; font-size: 56px; letter-spacing: -3px; fill: var(--lime); }
  .dj-joiner { fill: var(--cream); }
</style>
</head>
<body>
<svg class="flyer" viewBox="0 0 904 658" xmlns="http://www.w3.org/2000/svg">
  <defs>
    <linearGradient id="bg" x1="0" y1="0" x2="1" y2="0.45">
      <stop offset="0" stop-color="var(--green)"/>
      <stop offset="0.45" stop-color="var(--aqua)"/>
      <stop offset="0.85" stop-color="var(--cyan)"/>
    </linearGradient>
    <linearGradient id="photoTone" x1="0" y1="0" x2="1" y2="1">
      <stop offset="0" stop-color="var(--photo-light)"/>
      <stop offset="0.5" stop-color="var(--photo-mid)"/>
      <stop offset="1" stop-color="var(--photo-shade)"/>
    </linearGradient>
  </defs>

  <rect class="flyer-background" width="904" height="658" fill="url(#bg)"/>
  <path class="hero-photo" role="img" aria-label="Photo: woman in plaid shirt and denim shorts wearing a leather tool belt with wrenches, pliers and a hammer, tinted green" d="M0 0 H370 C380 180 390 330 400 470 C405 560 395 620 380 658 H0 Z" fill="url(#photoTone)"/>

  <text class="wordmark" x="846" y="200" text-anchor="end">forge</text>
  <text class="date" x="844" y="278" text-anchor="end">Saturday 12 March 2016</text>
  <text class="venue" x="844" y="340" text-anchor="end">NOVAlounge</text>

  <text class="tagline" x="846" y="423" text-anchor="end">w/ house and tech workers</text>
  <text class="dj" x="844" y="487" text-anchor="end">PARALLAX</text>
  <text class="dj" x="844" y="541" text-anchor="end">MR. HALVERTON</text>
  <text class="dj" x="844" y="595" text-anchor="end"><tspan class="dj-joiner">AND</tspan> DESMOND K. FARLEY</text>
</svg>
</body>
</html>
```